Clean Plinth Ads Banner Design For A Finance Company

Hi,
We're a UK based finance company and are looking for new banner ads to use on the Plinth Display Network.
We want the end product to stand out by using strong, minimal design - ideally starting from a dark theme, although I'm open to ideas.
The copy should read:
'Fast Bridging Loans From 0.39% PM'
Once we have these designs agreed, we are looking to replicate them for other products, changing only the text on each ad - for example, 'commercial mortgage service you can rely on' or 'development finance service you can rely on'.
The colours used on our website are the following:
Black - #040303
Orange - #f79124
White - #ffffff
Grey - #ffffff
Example ads that I like - https://www.brimcastle.com/wp-content/uploads/2021/07/plinth-display-ads-example-2-final.png.webp
2 - https://quendrahub.com/wp-content/uploads/2020/03/fbdd56ba3bd16c7a8debb13a411de786.jpg

```html
<!DOCTYPE html>
<html lang="en">
<head>
<meta charset="utf-8">
<title>Corvane Finance – Bridging Loan Banner Set</title>
<link rel="stylesheet" href="https://fonts.googleapis.com/css2?family=Montserrat:wght@800&family=Open+Sans:wght@400;600&display=swap">
<style>
  :root {
    --black: #040303;
    --orange: #f79124;
    --white: #ffffff;
    --stage: #2e2e2e;
    --photo-light: #8a8a8a;
    --photo-mid: #3a3a3a;
  }
  * { box-sizing: border-box; margin: 0; padding: 0; }
  html, body { width: 1200px; height: 1131px; overflow: hidden; background: var(--stage); }
  body { position: relative; font-family: "Open Sans", sans-serif; color: var(--white); }

  .banner { position: absolute; background: var(--black); overflow: hidden; }
  .banner > * { position: absolute; }

  .city-photo { background: radial-gradient(ellipse at 55% 20%, var(--photo-light) 0%, var(--photo-mid) 45%, var(--black) 100%); }

  .brand { font-family: "Montserrat", sans-serif; font-weight: 800; color: var(--orange); line-height: 1; text-align: center; }
  .headline { font-family: "Montserrat", sans-serif; font-weight: 800; line-height: 1.08; white-space: nowrap; }
  .headline .rate { color: var(--orange); display: block; }
  .tagline { font-size: 11.5px; letter-spacing: .06em; line-height: 1.3; }
  .divider { display: flex; gap: 6px; }
  .divider i { display: block; height: 3px; background: var(--orange); }
  .divider i + i { background: var(--white); }
  .web { letter-spacing: .32em; }
  .web b { color: var(--orange); font-weight: 400; }
  .call-label { font-size: 13px; }
  .call-number { font-weight: 600; color: var(--orange); }
  .cta {
    display: flex; align-items: center; justify-content: center; gap: 14px;
    background: var(--orange); color: var(--white); border-radius: 20px;
    font-family: "Montserrat", sans-serif; font-weight: 800; letter-spacing: .18em;
  }
  .cta svg { display: block; }
  .arrows { display: block; }
  .center { text-align: center; }
</style>
</head>
<body>

<svg width="0" height="0" style="position:absolute">
  <defs>
    <symbol id="arrow-trio" viewBox="0 0 54 12">
      <polygon points="0,0 11,6 0,12" fill="#ffffff"/>
      <polygon points="20,0 31,6 20,12" fill="#ffffff"/>
      <polygon points="40,0 51,6 40,12" fill="#f79124"/>
    </symbol>
    <symbol id="play" viewBox="0 0 20 20">
      <circle cx="10" cy="10" r="9" fill="#ffffff"/>
      <polygon points="8,5.5 14,10 8,14.5" fill="#f79124"/>
    </symbol>
  </defs>
</svg>

<!-- Skyscraper -->
<section class="banner skyscraper" style="left:68px;top:77px;width:409px;height:817px;">
  <div class="city-photo" role="img" aria-label="Black and white photo of skyscrapers seen from street level" style="left:0;top:0;width:409px;height:280px;-webkit-mask-image:linear-gradient(#000 75%,transparent);mask-image:linear-gradient(#000 75%,transparent);"></div>
  <div class="brand" style="left:0;top:318px;width:409px;font-size:50px;">Corvane<br><span style="font-size:22px;">Finance</span></div>
  <svg class="arrows" style="left:37px;top:414px;" width="54" height="12"><use href="#arrow-trio"/></svg>
  <div class="headline center" style="left:0;top:452px;width:409px;font-size:28px;">FAST BRIDGING<br><span style="font-size:47px;">LOANS</span><span class="rate" style="font-size:28px;margin-top:2px;">FROM 0.39% PM'</span></div>
  <p class="tagline center" style="left:0;top:582px;width:409px;">'Commercial Mortgage Service You Can Rel On' Or<br>'Development Finance Service</p>
  <div class="divider" style="left:178px;top:622px;"><i style="width:34px"></i><i style="width:14px"></i></div>
  <p class="call-label center" style="left:0;top:638px;width:409px;font-size:14px;">CALL NOW:-</p>
  <p class="call-number center" style="left:0;top:655px;width:409px;font-size:19px;">1100-222-999</p>
  <p class="web center" style="left:0;top:683px;width:409px;font-size:16px;">www.<b>corvane</b>.com</p>
  <a class="cta" style="left:134px;top:735px;width:146px;height:32px;font-size:10px;">CLICK HERE<svg width="17" height="17"><use href="#play"/></svg></a>
  <svg class="arrows" style="left:300px;top:791px;" width="42" height="10"><use href="#arrow-trio"/></svg>
</section>

<!-- Wide leaderboard -->
<section class="banner leaderboard" style="left:518px;top:82px;width:613px;height:191px;">
  <div class="city-photo" role="img" aria-label="Black and white photo of skyscrapers seen from street level" style="left:0;top:0;width:340px;height:191px;-webkit-mask-image:linear-gradient(90deg,#000 65%,transparent);mask-image:linear-gradient(90deg,#000 65%,transparent);"></div>
  <div class="brand" style="left:12px;top:14px;font-size:20px;text-align:left;">Corvane<br><span style="font-size:9px;">Finance</span></div>
  <p class="call-label" style="left:22px;top:163px;font-size:6.5px;">CALL NOW:-</p>
  <p class="call-number" style="left:13px;top:171px;font-size:8.5px;">1100-222-999</p>
  <svg class="arrows" style="left:290px;top:20px;" width="30" height="7"><use href="#arrow-trio"/></svg>
  <div class="headline center" style="left:286px;top:40px;width:300px;font-size:19px;">FAST BRIDGING LOANS<span class="rate">FROM 0.39% PM'</span></div>
  <p class="tagline center" style="left:286px;top:86px;width:300px;font-size:7.5px;">'Commercial Mortgage Service You Can Rel On' Or<br>'Development Finance Service</p>
  <div class="divider" style="left:417px;top:111px;"><i style="width:28px;height:2px"></i><i style="width:12px;height:2px"></i></div>
  <p class="web center" style="left:286px;top:116px;width:300px;font-size:8.5px;">www.<b>corvane</b>.com</p>
  <a class="cta" style="left:402px;top:141px;width:76px;height:17px;font-size:5px;gap:6px;">CLICK HERE<svg width="9" height="9"><use href="#play"/></svg></a>
  <svg class="arrows" style="left:562px;top:166px;" width="36" height="8"><use href="#arrow-trio"/></svg>
</section>

<!-- Medium rectangle -->
<section class="banner rectangle" style="left:518px;top:359px;width:607px;height:506px;">
  <div class="city-photo" role="img" aria-label="Black and white photo of skyscrapers seen from street level" style="left:0;top:0;width:607px;height:400px;-webkit-mask-image:linear-gradient(#000 70%,transparent);mask-image:linear-gradient(#000 70%,transparent);"></div>
  <div class="brand" style="left:30px;top:26px;font-size:34px;text-align:left;">Corvane<br><span style="font-size:15px;">Finance</span></div>
  <p class="call-label" style="right:24px;top:20px;font-size:12.5px;">CALL NOW:-</p>
  <p class="call-number" style="right:20px;top:35px;font-size:16px;">1100-222-999</p>
  <svg class="arrows" style="left:257px;top:314px;" width="36" height="8"><use href="#arrow-trio"/></svg>
  <div class="headline" style="left:29px;top:354px;font-size:28px;">FAST BRIDGING LOANS<span class="rate">FROM 0.39% PM'</span></div>
  <p class="tagline" style="left:29px;top:417px;">'Commercial Mortgage Service You Can Rel On' Or<br>'Development Finance Service</p>
  <div class="divider" style="left:29px;top:455px;gap:10px;"><i style="width:70px"></i><i style="width:29px"></i></div>
  <p class="web" style="left:29px;top:466px;font-size:12px;">www.<b>corvane</b>.com</p>
  <svg class="arrows" style="left:470px;top:405px;" width="54" height="12"><use href="#arrow-trio"/></svg>
  <a class="cta" style="left:425px;top:447px;width:146px;height:33px;font-size:10px;">CLICK HERE<svg width="17" height="17"><use href="#play"/></svg></a>
</section>

<!-- Bottom leaderboard -->
<section class="banner strip" style="left:68px;top:921px;width:1063px;height:132px;">
  <div class="city-photo" role="img" aria-label="Black and white photo of skyscrapers seen from street level" style="left:220px;top:0;width:290px;height:132px;-webkit-mask-image:linear-gradient(90deg,transparent,#000 25%,#000 70%,transparent);mask-image:linear-gradient(90deg,transparent,#000 25%,#000 70%,transparent);"></div>
  <div class="brand" style="left:40px;top:28px;font-size:40px;text-align:left;">Corvane<br><span style="font-size:18px;">Finance</span></div>
  <svg class="arrows" style="left:420px;top:32px;" width="27" height="6"><use href="#arrow-trio"/></svg>
  <div class="headline center" style="left:487px;top:18px;width:300px;font-size:21px;">FAST BRIDGING LOANS<span class="rate">FROM 0.39% PM'</span></div>
  <p class="tagline center" style="left:487px;top:70px;width:300px;font-size:8.5px;">'Commercial Mortgage Service You Can Rel On' Or<br>'Development Finance Service</p>
  <div class="divider" style="left:608px;top:94px;"><i style="width:36px;height:2px"></i><i style="width:14px;height:2px"></i></div>
  <p class="web center" style="left:487px;top:99px;width:300px;font-size:10.5px;">www.<b>corvane</b>.com</p>
  <a class="cta" style="left:730px;top:103px;width:57px;height:12px;font-size:4px;gap:5px;">CLICK HERE<svg width="7" height="7"><use href="#play"/></svg></a>
  <svg class="arrows" style="left:844px;top:94px;" width="27" height="6"><use href="#arrow-trio"/></svg>
  <svg class="arrows" style="left:935px;top:18px;" width="27" height="6"><use href="#arrow-trio"/></svg>
  <p class="call-label" style="left:981px;top:10px;font-size:10px;">CALL NOW:-</p>
  <p class="call-number" style="left:966px;top:22px;font-size:13px;">1100-222-999</p>
</section>

</body>
</html>
```